Banner Ad Design

We require a banner ad design for 4 Brands.

Banner 1: Willowmere on the Brook
Please follow url http://www.seniorhavenresidences.example/index.php/willowmere-on-the-brook/welcome for art, logo, tagline.

Banner 2: Noble Trellis
Please follow url http://www.seniorhavenresidences.example/index.php/noble-trellis/welcome for art, logo, tagline.

Banner 3: Trellis Meadows
Please follow url http://www.seniorhavenresidences.example/index.php/trellis-meadows/welcome for art, logo, tagline.

Banner 4: Marbury Court
http://www.seniorhavenresidences.example/index.php/marbury-court/welcome

ALL Banners consists of - 1. LOGO, 2. TAGLINE: Experience and uncompromising Retirement Lifestyle. 3. CALL TO ACTION: View Images, Download the Brochure, Register for More.

Each brand must be broken into the following Sizes:

468 × 60
728 × 90
250 × 250
200 × 200
336 × 280
300 × 250
120 × 600
160 × 600
300 × 600
970 × 90
240 × 400
980 × 120
930 × 180
250 × 360
580 × 400
150kb max size

Target Market(s)

Seniors and their middle age children

Industry/Entity Type

Royal

Requirements
Must have
• 468 × 60
728 × 90
250 × 250
200 × 200
336 × 280
300 × 250
120 × 600
160 × 600
300 × 600
970 × 90
240 × 400
980 × 120
930 × 180
250 × 360
580 × 400
150kb max size
Nice to have
• large font for easy viewing - images of the experience
Should not have
• any pictures of decrepit people, or dying people - must be fun and vibrant.

```html
<!DOCTYPE html>
<html lang="en">
<head>
<meta charset="utf-8">
<title>Noble Trellis – Banner Set</title>
<link href="https://fonts.googleapis.com/css2?family=Oswald:wght@500;600&display=swap" rel="stylesheet">
<style>
:root{
  --backdrop:#2b160d;
  --plum:#6e1d4f;
  --plum-deep:#4a0f33;
  --plum-light:#8c2c68;
  --gold:#f7b21e;
  --gold-light:#ffd24a;
  --gold-dark:#e08a00;
  --white:#ffffff;
  --logo-ink:#7a1f55;
  --ink:#2a1a10;
}
*{margin:0;padding:0;box-sizing:border-box}
html,body{width:1200px;height:962px;overflow:hidden}
body{background:var(--backdrop);font-family:'Oswald',sans-serif;position:relative}
.banner{position:absolute;overflow:hidden;border:1px solid #120804;background:var(--plum)}
.banner-art{position:absolute;inset:0;width:100%;height:100%}
.logo-block{position:absolute;left:0;top:0;background:var(--white);display:flex;align-items:center;justify-content:center;gap:8px}
.logo-mark{width:18px;height:18px;border-radius:50%;background:var(--logo-ink);flex:none}
.logo-name{color:var(--logo-ink);font-weight:500;line-height:1;text-align:left;text-transform:uppercase;letter-spacing:.5px}
.logo-name small{display:block;font-size:.55em;letter-spacing:1px;margin-bottom:2px}
.headline{position:absolute;text-align:center;text-transform:uppercase;line-height:1.02;font-weight:600}
.headline .lead{display:block;color:var(--white);text-shadow:0 1px 2px rgba(0,0,0,.5)}
.headline .accent{display:block;color:var(--gold);text-shadow:0 2px 2px rgba(40,0,20,.7)}
.cta{position:absolute;display:flex;align-items:center;justify-content:center;gap:8px;border-radius:5px;
  background:linear-gradient(var(--gold-light),var(--gold) 55%,var(--gold-dark));border:1px solid #fff3b0;
  color:var(--ink);font-weight:500;text-transform:uppercase;font-size:13px;box-shadow:0 1px 3px rgba(0,0,0,.5)}
.cta-arrow{width:17px;height:17px;flex:none}
</style>
</head>
<body>

<!-- Leaderboard -->
<section class="banner leaderboard" style="left:130px;top:124px;width:848px;height:103px">
  <svg class="banner-art" viewBox="0 0 848 103" preserveAspectRatio="none">
    <defs>
      <linearGradient id="lbPlum" x1="0" y1="0" x2="0" y2="1"><stop offset="0" stop-color="#8c2c68"/><stop offset="1" stop-color="#4a0f33"/></linearGradient>
      <linearGradient id="lbPhoto" x1="0" y1="0" x2="1" y2="1"><stop offset="0" stop-color="#9fae6a"/><stop offset=".5" stop-color="#c9b9a4"/><stop offset="1" stop-color="#7f9a5c"/></linearGradient>
    </defs>
    <rect x="500" y="0" width="348" height="103" fill="url(#lbPhoto)" role="img" aria-label="Photo of smiling seniors together outdoors"/>
    <path d="M170 0H532Q508 52 528 103H170Z" fill="url(#lbPlum)"/>
    <path d="M532 0Q508 52 528 103" fill="none" stroke="#f7b21e" stroke-width="4"/>
  </svg>
  <div class="logo-block" style="width:170px;height:103px;align-items:flex-start;padding-top:16px">
    <span class="logo-mark"></span><span class="logo-name" style="font-size:20px"><small>Noble</small>Trellis</span>
  </div>
  <a class="cta" style="left:9px;top:65px;width:154px;height:30px;font-size:12px">Register for more
    <svg class="cta-arrow" viewBox="0 0 20 20"><circle cx="10" cy="10" r="9" fill="#1a1a1a"/><path d="M8 5l5 5-5 5" fill="none" stroke="#fff" stroke-width="2.4"/></svg></a>
  <h2 class="headline" style="left:170px;top:7px;width:354px">
    <span class="lead" style="font-size:20px">Experience an uncompromising</span>
    <span class="accent" style="font-size:31px;line-height:1">&amp; Affordable</span>
    <span class="accent" style="font-size:25px">Retirement Lifestyle</span>
  </h2>
</section>

<!-- Skyscraper -->
<section class="banner skyscraper" style="left:130px;top:250px;width:186px;height:699px">
  <svg class="banner-art" viewBox="0 0 186 699" preserveAspectRatio="none">
    <defs>
      <linearGradient id="skPlum" x1="0" y1="0" x2="0" y2="1"><stop offset="0" stop-color="#8c2c68"/><stop offset=".5" stop-color="#6e1d4f"/><stop offset="1" stop-color="#3e0c2b"/></linearGradient>
      <linearGradient id="skPhoto" x1="0" y1="0" x2="1" y2="1"><stop offset="0" stop-color="#8fa65a"/><stop offset=".45" stop-color="#d6ccbc"/><stop offset="1" stop-color="#a89a86"/></linearGradient>
    </defs>
    <rect width="186" height="699" fill="url(#skPlum)"/>
    <path d="M0 340Q70 300 186 312V640Q90 650 0 610Z" fill="url(#skPhoto)" role="img" aria-label="Photo of cheerful senior women chatting outdoors"/>
    <path d="M0 340Q70 300 186 312" fill="none" stroke="#f7b21e" stroke-width="4"/>
    <path d="M0 610Q90 650 186 640" fill="none" stroke="#f7b21e" stroke-width="4"/>
  </svg>
  <div class="logo-block" style="width:186px;height:84px">
    <span class="logo-mark"></span><span class="logo-name" style="font-size:24px"><small>Noble</small>Trellis</span>
  </div>
  <h2 class="headline" style="left:0;top:118px;width:186px">
    <span class="lead" style="font-size:21px;line-height:1.12">Experience an<br>uncompromising</span>
    <span class="accent" style="font-size:28px;margin-top:18px">&amp; Affordable</span>
    <span class="accent" style="font-size:35px;line-height:1.05">Retirement<br>Lifestyle</span>
  </h2>
  <a class="cta" style="left:10px;top:651px;width:166px;height:31px">Register for more
    <svg class="cta-arrow" viewBox="0 0 20 20"><circle cx="10" cy="10" r="9" fill="#1a1a1a"/><path d="M8 5l5 5-5 5" fill="none" stroke="#fff" stroke-width="2.4"/></svg></a>
</section>

<!-- Large rectangle -->
<section class="banner large-rect" style="left:340px;top:250px;width:391px;height:326px">
  <svg class="banner-art" viewBox="0 0 391 326" preserveAspectRatio="none">
    <defs>
      <linearGradient id="lrPlum" x1="0" y1="0" x2="0" y2="1"><stop offset="0" stop-color="#8c2c68"/><stop offset="1" stop-color="#3e0c2b"/></linearGradient>
      <linearGradient id="lrPhoto" x1="0" y1="0" x2="1" y2="1"><stop offset="0" stop-color="#8fa65a"/><stop offset=".45" stop-color="#d6ccbc"/><stop offset="1" stop-color="#a89a86"/></linearGradient>
    </defs>
    <rect x="190" width="201" height="326" fill="url(#lrPhoto)" role="img" aria-label="Photo of cheerful senior women chatting outdoors"/>
    <path d="M0 0H212Q200 170 242 326H0Z" fill="url(#lrPlum)"/>
    <path d="M212 0Q200 170 242 326" fill="none" stroke="#f7b21e" stroke-width="4"/>
  </svg>
  <div class="logo-block" style="width:209px;height:79px">
    <span class="logo-mark"></span><span class="logo-name" style="font-size:24px"><small>Noble</small>Trellis</span>
  </div>
  <h2 class="headline" style="left:0;top:95px;width:214px">
    <span class="lead" style="font-size:20px;line-height:1.12">Experience an<br>uncompromising</span>
    <span class="accent" style="font-size:27px;margin-top:5px">&amp; Affordable</span>
    <span class="accent" style="font-size:33px;line-height:1.05">Retirement<br>Lifestyle</span>
  </h2>
  <a class="cta" style="left:23px;top:277px;width:166px;height:30px">Register for more
    <svg class="cta-arrow" viewBox="0 0 20 20"><circle cx="10" cy="10" r="9" fill="#1a1a1a"/><path d="M8 5l5 5-5 5" fill="none" stroke="#fff" stroke-width="2.4"/></svg></a>
</section>

<!-- Medium rectangle -->
<section class="banner medium-rect" style="left:747px;top:285px;width:349px;height:291px">
  <svg class="banner-art" viewBox="0 0 349 291" preserveAspectRatio="none">
    <defs>
      <linearGradient id="mrPlum" x1="0" y1="0" x2="0" y2="1"><stop offset="0" stop-color="#8c2c68"/><stop offset="1" stop-color="#3e0c2b"/></linearGradient>
      <linearGradient id="mrPhoto" x1="0" y1="0" x2="1" y2="1"><stop offset="0" stop-color="#8fa65a"/><stop offset=".45" stop-color="#d6ccbc"/><stop offset="1" stop-color="#a89a86"/></linearGradient>
    </defs>
    <rect x="170" width="179" height="291" fill="url(#mrPhoto)" role="img" aria-label="Photo of cheerful senior women chatting outdoors"/>
    <path d="M0 0H186Q176 150 214 291H0Z" fill="url(#mrPlum)"/>
    <path d="M186 0Q176 150 214 291" fill="none" stroke="#f7b21e" stroke-width="4"/>
  </svg>
  <div class="logo-block" style="width:181px;height:71px">
    <span class="logo-mark"></span><span class="logo-name" style="font-size:22px"><small>Noble</small>Trellis</span>
  </div>
  <h2 class="headline" style="left:0;top:86px;width:186px">
    <span class="lead" style="font-size:18px;line-height:1.12">Experience an<br>uncompromising</span>
    <span class="accent" style="font-size:24px;margin-top:6px">&amp; Affordable</span>
    <span class="accent" style="font-size:29px;line-height:1.05">Retirement<br>Lifestyle</span>
  </h2>
  <a class="cta" style="left:21px;top:247px;width:149px;height:28px;font-size:12px">Register for more
    <svg class="cta-arrow" viewBox="0 0 20 20"><circle cx="10" cy="10" r="9" fill="#1a1a1a"/><path d="M8 5l5 5-5 5" fill="none" stroke="#fff" stroke-width="2.4"/></svg></a>
</section>

</body>
</html>
```